Business Card Design Project

I run holistic health workshops, speaking engagements, group and 1on1 coaching, cooking classes, and am a speaker and presenter on holistic health topics.

I would like professionally designed business cards using the attached logo. I would like the reverse of the cards to use the leaf pattern blown up large across the back of the card as the design. I'd also like to use the words "rest.move.grow.nourish" across the backside of the cards.

The front of the cards should contain the following contact details:
Megan Thorsby-Kell
Founder & President
The Harwick Advisory Group
+61 477 392 604
theharwickadvisorygroup@mailbrook.example

Target Market(s)

Corporate HR, Health & wellness businesses, upmarket spas, other businesses in the holistic health & wellness fields looking for a speaker/presenter/workshop leader

Industry/Entity Type

Cooking

Requirements
Must have
• Must use the attached design; must use earth tones in line with the logo (browns/greens/blues/tans)

```html
<!DOCTYPE html>
<html lang="en">
<head>
<meta charset="utf-8">
<title>Harwick Group Business Card</title>
<link rel="stylesheet" href="https://fonts.googleapis.com/css2?family=Source+Sans+3:wght@300;400&display=swap">
<style>
  :root {
    --canvas-bg: #e9e9e9;
    --card-bg: #ffffff;
    --ink: #4a4a4a;
    --ink-soft: #5a5a5a;
    --leaf-light: #a9d38a;
    --leaf-mid: #6fb444;
    --leaf-dark: #2f8f3c;
    --card-shadow: rgba(0, 0, 0, 0.28);
  }
  * { box-sizing: border-box; margin: 0; padding: 0; }
  html, body {
    width: 1109px;
    height: 1200px;
    overflow: hidden;
    background: var(--canvas-bg);
    font-family: "Source Sans 3", "Myriad Pro", sans-serif;
    color: var(--ink);
  }
  .canvas {
    position: relative;
    width: 1109px;
    height: 1200px;
  }
  .card {
    position: absolute;
    left: 114px;
    width: 880px;
    height: 508px;
    background: var(--card-bg);
    box-shadow: 0 6px 14px var(--card-shadow);
    overflow: hidden;
  }
  .card--front { top: 62px; }
  .card--back { top: 630px; }

  /* Front */
  .brand {
    position: absolute;
    left: 60px;
    top: 64px;
  }
  .brand__row {
    display: flex;
    align-items: center;
    gap: 12px;
  }
  .brand__dot {
    width: 30px;
    height: 30px;
    border-radius: 50%;
    background: var(--leaf-mid);
  }
  .brand__name {
    font-size: 54px;
    font-weight: 400;
    line-height: 1;
    color: var(--ink);
    letter-spacing: -0.5px;
  }
  .brand__tagline {
    margin-top: 8px;
    font-size: 12.5px;
    font-weight: 400;
    color: var(--ink);
  }
  .holder {
    position: absolute;
    right: 68px;
    top: 204px;
    text-align: right;
  }
  .holder__name {
    font-size: 41px;
    font-weight: 400;
    line-height: 1.05;
    color: var(--ink);
  }
  .holder__title {
    font-size: 17px;
    font-weight: 400;
    color: var(--ink);
  }
  .contact {
    position: absolute;
    left: 59px;
    top: 366px;
    list-style: none;
    font-size: 25px;
    font-weight: 300;
    line-height: 34px;
    color: var(--ink-soft);
  }

  /* Back */
  .leaf-field {
    position: absolute;
    inset: 0;
    background:
      linear-gradient(135deg, var(--leaf-light) 0%, var(--leaf-mid) 50%, var(--leaf-dark) 100%);
  }
  .glow {
    position: absolute;
    inset: 0;
    background: radial-gradient(ellipse 300px 200px at 50% 52%,
      rgba(255,255,255,1) 0%, rgba(255,255,255,0.95) 45%, rgba(255,255,255,0) 100%);
  }
  .back-mark {
    position: absolute;
    left: 50%;
    top: 50%;
    transform: translate(-50%, -50%);
    text-align: center;
  }
  .back-mark__row {
    display: flex;
    align-items: center;
    justify-content: center;
    gap: 16px;
  }
  .back-mark__dot {
    width: 40px;
    height: 40px;
    border-radius: 50%;
    background: var(--leaf-mid);
  }
  .back-mark__name {
    font-size: 82px;
    font-weight: 400;
    line-height: 1;
    color: var(--ink);
    letter-spacing: -1px;
  }
  .back-mark__motto {
    margin-top: 12px;
    font-size: 21px;
    font-weight: 400;
    color: var(--ink);
    letter-spacing: 0.5px;
  }
</style>
</head>
<body>
<main class="canvas">
  <section class="card card--front">
    <div class="brand">
      <div class="brand__row">
        <span class="brand__dot"></span>
        <span class="brand__name">Harwick</span>
      </div>
      <p class="brand__tagline">the harwick advisory group</p>
    </div>
    <div class="holder">
      <p class="holder__name">Megan Thorsby-Kell</p>
      <p class="holder__title">Founder &amp; President</p>
    </div>
    <ul class="contact">
      <li>The Harwick Advisory Group</li>
      <li>+61 477 392 604</li>
      <li>theharwickadvisorygroup@mailbrook.example</li>
    </ul>
  </section>

  <section class="card card--back">
    <div class="leaf-field" role="img" aria-label="Repeating pattern of green leaf motifs covering the card"></div>
    <div class="glow"></div>
    <div class="back-mark">
      <div class="back-mark__row">
        <span class="back-mark__dot"></span>
        <span class="back-mark__name">Harwick</span>
      </div>
      <p class="back-mark__motto">rest.move.grow.nourish</p>
    </div>
  </section>
</main>
</body>
</html>
```